Bellcroft construction website for a high end luxury custom home builder

I need a website designed for a high end luxury custom home builder. I would like the website to host a number activities. A blog/vlog on the page where I can post about the projects being built how to's what to look out for during the build, A designated testimonial page but also having testimonials posted on the other pages like the gallery linked to the photos of the completed projects. a gallery page, an about us page, services page that demonstrate what we do and what we are capable of, and hopefully when I start winning awards, and awards page.
Home page
about us page
services page
gallery
testimonial
awards page but I my need to add that later.
I already have the domain name for the website. www.bellcroftconstruction.com.au
I recently completed a sketch hive page for my logo and will post the logo documents below.

Target Market(s)

I'd like to target professions with cash enough to build a house. I would like peolpe to understand that they are buy a price when they are getting quote to build there house. It seems like people just look for the cheapest price and end up with an inferior product. Where as people need to understand that a builder with the high price ( not astronomically higher 15-20% higher) are the ones with correct systems in place, a bide by correct OHS and use proper and correct product. If that can be conveyed through the website somehow, without saying it directly, it would be awesome.

Industry/Entity Type

Residential Construction

Coding

Coded - Design and coding required

Number of Pages Required

5+ page

Font styles to use
Sans Serif

Requirements
Must have
• I would like the testimonials to have a designated page (mentioned in the brief) but I would like the testimonials to be linked to the gallery page and when the picture are open of completed job the relevant testimonials would pop up near the pictures.

Nice to have
• I would like peolpe to understand that they are buy a price when they are getting quote to build there house. It seems like people just look for the cheapest price and end up with an inferior product. Where as people need to understand that a builder with the high price ( not astronomically higher 15-20% higher) are the ones with correct systems in place, a bide by correct OHS and use proper and correct product. If that can be conveyed through the website somehow, without saying it directly, it would be awesome.

```html
<!DOCTYPE html>
<html lang="en">
<head>
<meta charset="utf-8">
<title>Bellcroft Construction</title>
<link href="https://fonts.googleapis.com/css2?family=Montserrat:wght@400;500;600&family=Tinos:wght@400;700&display=swap" rel="stylesheet">
<style>
:root{
  --blue:#1f6fbf;
  --blue-dark:#1a5fa6;
  --grey:#58595b;
  --grey-dark:#4b4c4e;
  --ink:#333;
  --muted:#555;
  --light:#f4f6f9;
  --white:#fff;
}
*{margin:0;padding:0;box-sizing:border-box}
html,body{width:1200px;height:4552px;overflow:hidden}
body{position:relative;font-family:'Montserrat',sans-serif;color:var(--ink);background:var(--white)}
.abs{position:absolute}
.serif{font-family:'Tinos',serif}
.btn{position:absolute;display:flex;align-items:center;justify-content:center;border-radius:20px;background:var(--blue);color:#fff;font-size:12px;font-weight:500;letter-spacing:.5px;text-transform:uppercase}
.btn.dark{background:var(--grey)}
.ph{position:absolute}
.section-title{position:absolute;left:0;width:1200px;text-align:center;font-family:'Tinos',serif;font-size:32px;letter-spacing:2px;color:#444}
.brand{position:absolute;display:flex;align-items:center;gap:10px}
.brand .mark{width:38px;height:38px;border:3px solid var(--blue);border-radius:50%}
.brand .name{font-family:'Tinos',serif;font-weight:700;font-size:26px;color:var(--blue);letter-spacing:1px;line-height:1}
.head-contact{position:absolute;display:flex;align-items:center;gap:10px;font-size:11px;line-height:1.3}
.head-contact .ic{width:30px;height:30px;border-radius:50%;background:var(--blue);display:flex;align-items:center;justify-content:center}
.head-contact .lab{color:var(--blue)}
.nav{position:absolute;left:0;top:118px;width:1200px;height:53px;background:var(--blue)}
.nav ul{list-style:none;display:flex;position:absolute;left:76px;top:0;height:53px}
.nav li{height:53px;display:flex;align-items:center;justify-content:center;color:#fff;font-size:13px;font-weight:500;letter-spacing:1.5px;border-right:1px solid rgba(255,255,255,.25)}
.nav li.active{background:var(--grey)}
.hero{position:absolute;left:0;top:171px;width:1200px;height:586px;background:linear-gradient(180deg,#dfe8f1,#eef2f6)}
.hero h1{position:absolute;left:74px;font-family:'Tinos',serif;color:#3a3a3a;font-weight:700;letter-spacing:1.5px}
.hero p{position:absolute;left:74px;top:268px;width:340px;font-size:13px;color:var(--muted);line-height:1.45}
.svc{position:absolute;top:1496px;width:303px;height:282px;background:#fff;text-align:center}
.svc h3{font-family:'Tinos',serif;font-size:18px;letter-spacing:1px;color:#333;margin-top:16px}
.svc p{font-size:12.5px;color:var(--muted);line-height:1.5;padding:0 30px;margin-top:10px}
.post{position:absolute;top:3413px;width:305px;text-align:center}
.post .img{height:233px}
.post h4{font-family:'Tinos',serif;font-size:15px;color:#444;margin-top:26px}
.post .rule{width:120px;height:1px;background:#999;margin:10px auto}
.post p{font-size:11.5px;color:var(--muted);line-height:1.4;padding:0 30px}
.post .date{font-size:12.5px;color:#333;margin-top:20px;display:flex;gap:8px;justify-content:center;align-items:center}
.footer{position:absolute;left:0;top:4100px;width:1200px;height:452px;background:var(--grey);color:#fff}
.footer h5{position:absolute;top:94px;font-family:'Tinos',serif;font-weight:400;font-size:17px}
.footer ul{position:absolute;top:142px;list-style:none;font-size:13px;line-height:21px;letter-spacing:1px}
.field{position:absolute;border:1px solid #6f7072;background:var(--grey-dark);font-size:12px;padding:6px 8px;color:#ddd}
.social{position:absolute;top:4477px;width:40px;height:40px;border-radius:50%;background:var(--blue)}
</style>
</head>
<body>

<div class="brand" style="left:74px;top:30px">
  <span class="mark"></span><span class="name">BELLCROFT<br><span style="font-size:11px;letter-spacing:3px;color:#444">CONSTRUCTION</span></span>
</div>
<div class="head-contact" style="left:580px;top:44px">
  <span class="ic"><svg width="14" height="10" viewBox="0 0 14 10"><rect x=".5" y=".5" width="13" height="9" fill="none" stroke="#fff"/><path d="M.5 .5 7 6 13.5 .5" fill="none" stroke="#fff"/></svg></span>
  <span><span class="lab">Email us Now</span><br>hello@bellcroftbuild.com</span>
</div>
<div class="head-contact" style="left:785px;top:44px">
  <span class="ic"><svg width="14" height="14" viewBox="0 0 24 24"><path fill="#fff" d="M6.6 10.8a15 15 0 0 0 6.6 6.6l2.2-2.2c.3-.3.7-.4 1-.2 1.1.4 2.3.6 3.6.6.6 0 1 .4 1 1V20c0 .6-.4 1-1 1A17 17 0 0 1 3 4c0-.6.4-1 1-1h3.5c.6 0 1 .4 1 1 0 1.3.2 2.5.6 3.6.1.3 0 .7-.2 1z"/></svg></span>
  <span><span class="lab">Call us Today</span><br>+61 2 5550 1842</span>
</div>
<div class="btn" style="left:969px;top:44px;width:155px;height:32px">Get a Quote</div>

<nav class="nav">
  <ul>
    <li class="active" style="width:148px">HOME</li>
    <li style="width:102px">ABOUT</li>
    <li style="width:143px">SERVICES</li>
    <li style="width:143px">GALLERY</li>
    <li style="width:106px">BLOG</li>
    <li style="width:170px">TESTIMONIALS</li>
    <li style="width:148px;border:none">CONTACT</li>
  </ul>
  <svg class="abs" style="left:1106px;top:17px" width="19" height="19" viewBox="0 0 20 20"><circle cx="8" cy="8" r="6" fill="none" stroke="#fff" stroke-width="2"/><path d="M12.5 12.5 18 18" stroke="#fff" stroke-width="2"/></svg>
</nav>

<section class="hero">
  <div class="ph" role="img" aria-label="Modern white multi-storey building with glass balconies" style="left:500px;top:0;width:700px;height:586px;background:linear-gradient(135deg,#c9d6e3 0%,#f3f5f7 40%,#b9c6d3 75%,#6f8a5f 100%)"></div>
  <h1 style="top:172px;font-size:28px;font-weight:400">WE TAKE CARE</h1>
  <h1 style="top:210px;font-size:38px">OF YOUR HOME</h1>
  <p>Lorem Ipsum is simply dummy ever text printing and typesetting a ever since the 1500s</p>
  <div class="btn" style="left:74px;top:333px;width:156px;height:33px">Get a Quote</div>
  <div class="btn dark" style="left:244px;top:333px;width:156px;height:33px">Contact Us</div>
  <div class="abs" style="left:92px;top:503px;display:flex;align-items:center;gap:6px;font-size:12px;color:#333">
    <svg width="26" height="10" viewBox="0 0 26 10"><path d="M26 5H2M6 1 2 5l4 4" fill="none" stroke="#333" stroke-width="2"/></svg>1/4
    <svg width="26" height="10" viewBox="0 0 26 10"><path d="M0 5h24M20 1l4 4-4 4" fill="none" stroke="#1f6fbf" stroke-width="2"/></svg>
  </div>
</section>

<h2 class="section-title" style="top:828px;font-weight:400">ABOUT US</h2>
<div class="ph" role="img" aria-label="Glass office tower" style="left:118px;top:893px;width:260px;height:287px;background:linear-gradient(160deg,#8ea2b8,#3c4c63 60%,#b7c4d2)"></div>
<div class="ph" style="left:300px;top:950px;width:284px;height:310px;background:#fff"></div>
<div class="ph" role="img" aria-label="Dark high-rise building at dusk" style="left:312px;top:962px;width:260px;height:286px;background:linear-gradient(180deg,#b9cadb,#1d2a3d 55%,#0f1624)"></div>
<div class="ph" style="left:272px;top:1193px;width:24px;height:24px;background:var(--blue)"></div>
<h3 class="abs serif" style="left:620px;top:904px;font-size:28px;font-weight:400;color:#444">Bellcroft Construction</h3>
<div class="abs" style="left:620px;top:966px;width:40px;height:3px;background:var(--blue)"></div>
<div class="abs" style="left:620px;top:988px;width:480px;font-size:11.5px;line-height:1.55;color:var(--muted)">
  <p>Lorem Ipsum is simply dummy text of the printing and typesetting industry has been the industry's standard dummy text ever since the 1500s,</p>
  <p style="margin-top:18px">when an unknown printer took a galley of type and scrambled it to make a type specimen book. It has survived not only five centuries, but also the leap into electronic typesetting, remaining essentially unchanged. It was popularised industries arein the 1960s</p>
  <p style="margin-top:18px">with the release of Inkpress sheets containing Lorem Ipsum passages, and more recently with desktop publishing software like Pagecraft Studio including ipsum text versions of Lorem Ipsum.</p>
</div>
<div class="btn" style="left:616px;top:1209px;width:156px;height:32px">Read More</div>

<section class="abs" style="left:0;top:1365px;width:1200px;height:578px;background:var(--grey)"></section>
<h2 class="section-title" style="top:1418px;color:#fff;font-weight:400">SERVICES</h2>
<div class="svc" style="left:112px">
  <svg style="margin-top:34px" width="74" height="80" viewBox="0 0 74 80" fill="none" stroke="#1f6fbf" stroke-width="2"><path d="M4 34 37 6l33 28M12 28v48h50V28"/><rect x="30" y="52" width="14" height="24"/><rect x="18" y="36" width="10" height="10"/><rect x="46" y="36" width="10" height="10"/><rect x="32" y="20" width="10" height="10"/></svg>
  <h3>LUXURY CONSTRUCTION</h3>
  <p>Lorem Ipsum is simply dummy ever text printing and typesetting a ever since the 1500s</p>
  <svg style="margin-top:14px" width="28" height="12" viewBox="0 0 28 12"><path d="M0 6h25M20 1l5 5-5 5" fill="none" stroke="#1f6fbf" stroke-width="2.5"/></svg>
</div>
<div class="svc" style="left:448px">
  <svg style="margin-top:44px" width="104" height="70" viewBox="0 0 104 70" fill="none" stroke="#1f6fbf" stroke-width="2"><path d="M2 28 20 4l18 24M34 28 52 4l18 24M66 28 84 4l18 24M6 24v44h92V24"/><rect x="14" y="44" width="10" height="24"/><rect x="47" y="44" width="10" height="24"/><rect x="80" y="44" width="10" height="24"/><rect x="15" y="26" width="10" height="8"/><rect x="47" y="26" width="10" height="8"/><rect x="79" y="26" width="10" height="8"/></svg>
  <h3>BUILDING HOMES</h3>
  <p>Lorem Ipsum is simply dummy ever text printing and typesetting a ever since the 1500s</p>
</div>
<div class="svc" style="left:783px">
  <svg style="margin-top:42px" width="76" height="76" viewBox="0 0 76 76" fill="none" stroke="#1f6fbf" stroke-width="2"><rect x="22" y="4" width="22" height="70"/><rect x="44" y="22" width="26" height="52"/><rect x="28" y="12" width="5" height="6"/><rect x="35" y="12" width="5" height="6"/><rect x="28" y="24" width="5" height="6"/><rect x="35" y="24" width="5" height="6"/><rect x="52" y="30" width="8" height="6"/><rect x="52" y="44" width="8" height="6"/><rect x="52" y="58" width="8" height="6"/><circle cx="12" cy="50" r="9"/><path d="M12 59v15M4 74h68"/></svg>
  <h3>MULTI STOREY</h3>
  <p>Lorem Ipsum is simply dummy ever text printing and typesetting a ever since the 1500s</p>
  <svg style="margin-top:14px" width="28" height="12" viewBox="0 0 28 12"><path d="M0 6h25M20 1l5 5-5 5" fill="none" stroke="#1f6fbf" stroke-width="2.5"/></svg>
</div>
<div class="btn" style="left:530px;top:1840px;width:155px;height:30px">View More</div>

<h2 class="section-title" style="top:2003px;font-weight:400">GALLERY</h2>
<div class="ph" role="img" aria-label="Mediterranean style villa with garden" style="left:113px;top:2085px;width:311px;height:246px;background:linear-gradient(180deg,#5d8fc4,#b49a78 55%,#3d5a2e)"></div>
<div class="ph" role="img" aria-label="White modern apartment facade" style="left:445px;top:2085px;width:311px;height:513px;background:linear-gradient(160deg,#d7dfe7,#f5f6f7 50%,#c8d0d8)"></div>
<div class="ph" role="img" aria-label="Luxury home with pool at dusk" style="left:776px;top:2085px;width:310px;height:246px;background:linear-gradient(180deg,#4a78b0,#e3e3e0 50%,#2a6fb5)"></div>
<div class="ph" role="img" aria-label="Family home at night" style="left:113px;top:2352px;width:311px;height:246px;background:linear-gradient(180deg,#2c2c2c,#151515)"></div>
<svg class="abs" style="left:246px;top:2458px" width="32" height="32" viewBox="0 0 32 32" fill="none" stroke="#fff" stroke-width="2"><path d="M2 10V2h8M22 2h8v8M30 22v8h-8M10 30H2v-8M16 10v12M10 16h12"/></svg>
<div class="abs" style="left:128px;top:2526px;color:#fff">
  <div class="serif" style="font-size:15px;font-weight:700">Projeact Name</div>
  <div style="font-size:12px;line-height:1.5;margin-top:4px">Lorem Ipsum is simply dummy ever text<br>since the 1500s</div>
</div>
<div class="ph" role="img" aria-label="Dark brick building corner against blue sky" style="left:776px;top:2352px;width:310px;height:246px;background:linear-gradient(160deg,#2f55a0,#3e4450 55%,#2a2d33)"></div>
<div class="btn" style="left:522px;top:2628px;width:145px;height:30px">View More</div>

<section class="abs" style="left:0;top:2743px;width:1200px;height:535px;background:var(--blue)"></section>
<h2 class="section-title" style="top:2810px;color:#fff;font-weight:400">TESTIMONIAL</h2>
<div class="ph" role="img" aria-label="Modern two-storey house with pool" style="left:270px;top:2890px;width:298px;height:268px;background:linear-gradient(180deg,#dfe6ee,#c49a82 55%,#5ea9c9)"></div>
<svg class="abs" style="left:399px;top:3024px" width="32" height="32" viewBox="0 0 32 32"><circle cx="16" cy="16" r="14" fill="none" stroke="#fff" stroke-width="2"/><path d="M13 10v12l9-6z" fill="#fff"/></svg>
<div class="ph" role="img" aria-label="Client portrait" style="left:525px;top:2996px;width:88px;height:88px;border-radius:50%;border:4px solid #fff;background:linear-gradient(180deg,#9fb7d0,#6a7f99)"></div>
<div class="abs" style="left:637px;top:2943px;color:#fff">
  <div class="serif" style="font-size:16px">Daniel Morrow</div>
  <div style="font-size:11px;margin-top:10px">Director</div>
  <p style="width:370px;font-size:10.5px;line-height:1.4;margin-top:22px">Lorem Ipsum is simply dummy text of the printing and typesetting industry. Lorem Ipsum has been the industry's standard dummy text ever since the 1500s, when an unknown printer took a galley of type and scrambled it to make a type specimen book. It has survived not only five centuries,</p>
  <div style="color:#ffd200;font-size:24px;letter-spacing:2px;margin-top:6px">★★★★★</div>
</div>
<svg class="abs" style="left:146px;top:3026px" width="34" height="34" viewBox="0 0 34 34" fill="none" stroke="#fff" stroke-width="1.5"><circle cx="17" cy="17" r="15"/><path d="M19 11l-6 6 6 6"/></svg>
<svg class="abs" style="left:1060px;top:3026px" width="34" height="34" viewBox="0 0 34 34" fill="none" stroke="#fff" stroke-width="1.5"><circle cx="17" cy="17" r="15"/><path d="M15 11l6 6-6 6"/></svg>

<h2 class="section-title" style="top:3330px;font-weight:400">BLOGS</h2>
<div class="post" style="left:115px">
  <div class="img" role="img" aria-label="Suburban house at sunset" style="background:linear-gradient(180deg,#6d6fa0,#d7a98e 45%,#2f3a5c)"></div>
  <h4>Blog Heading 01</h4><div class="rule"></div>
  <p>Lorem Ipsum is simply next dummy text in the industry's standard dummy.</p>
  <div class="date"><svg width="14" height="14" viewBox="0 0 14 14" fill="none" stroke="#1f6fbf"><rect x="1" y="2" width="12" height="11"/><path d="M1 5h12M4 0v3M10 0v3"/></svg>June 30, 2020</div>
</div>
<div class="post" style="left:447px">
  <div class="img" role="img" aria-label="Looking up at a tall apartment block" style="background:linear-gradient(160deg,#2f5f9a,#9aa7b5 50%,#3f4a58)"></div>
  <h4>Blog Heading 01</h4><div class="rule"></div>
  <p>Lorem Ipsum is simply next dummy text in the industry's standard dummy.</p>
  <div class="date"><svg width="14" height="14" viewBox="0 0 14 14" fill="none" stroke="#1f6fbf"><rect x="1" y="2" width="12" height="11"/><path d="M1 5h12M4 0v3M10 0v3"/></svg>June 30, 2020</div>
</div>
<div class="post" style="left:780px">
  <div class="img" role="img" aria-label="Row of Victorian style houses" style="background:linear-gradient(180deg,#9fc1e0,#c7b8a8 45%,#587a3b)"></div>
  <h4>Blog Heading 01</h4><div class="rule"></div>
  <p>Lorem Ipsum is simply next dummy text in the industry's standard dummy.</p>
  <div class="date"><svg width="14" height="14" viewBox="0 0 14 14" fill="none" stroke="#1f6fbf"><rect x="1" y="2" width="12" height="11"/><path d="M1 5h12M4 0v3M10 0v3"/></svg>June 30, 2020</div>
</div>
<svg class="abs" style="left:252px;top:3513px" width="30" height="30" viewBox="0 0 32 32"><circle cx="16" cy="16" r="14" fill="none" stroke="#fff" stroke-width="2"/><path d="M13 10v12l9-6z" fill="#fff"/></svg>
<svg class="abs" style="left:584px;top:3513px" width="30" height="30" viewBox="0 0 32 32"><circle cx="16" cy="16" r="14" fill="none" stroke="#fff" stroke-width="2"/><path d="M13 10v12l9-6z" fill="#fff"/></svg>
<svg class="abs" style="left:917px;top:3513px" width="30" height="30" viewBox="0 0 32 32"><circle cx="16" cy="16" r="14" fill="none" stroke="#fff" stroke-width="2"/><path d="M13 10v12l9-6z" fill="#fff"/></svg>
<div class="btn" style="left:518px;top:3843px;width:148px;height:30px">View More</div>

<h2 class="section-title" style="top:3920px;font-size:28px;letter-spacing:.5px;font-weight:400">Subscribe Our Newsletter</h2>
<p class="abs" style="left:0;top:3960px;width:1200px;text-align:center;font-size:11.5px;color:var(--muted)">Lorem Ipsum is simply next dummy</p>
<div class="abs" style="left:342px;top:3996px;width:380px;height:36px;background:#f1f1f1;border-radius:18px 0 0 18px;font-size:11px;color:#777;padding:11px 22px">Email Here</div>
<div class="abs" style="left:722px;top:3996px;width:125px;height:36px;background:var(--blue);border-radius:0 18px 18px 0;color:#fff;font-size:11px;display:flex;align-items:center;justify-content:center">SUBSCRIBE</div>

<footer class="footer">
  <div class="brand" style="left:74px;top:180px">
    <span class="mark" style="border-color:#fff"></span><span class="name" style="color:#fff">BELLCROFT<br><span style="font-size:11px;letter-spacing:3px">CONSTRUCTION</span></span>
  </div>
  <h5 style="left:385px">Quick Link</h5>
  <ul style="left:385px">
    <li>&gt;&nbsp; Home</li><li>&gt;&nbsp; About</li><li>&gt;&nbsp; Services</li><li>&gt;&nbsp; gallery</li><li>&gt;&nbsp; BLog</li><li>&gt;&nbsp; Testimonials</li><li>&gt;&nbsp; Contact</li>
  </ul>
  <h5 style="left:575px">Contact info</h5>
  <div class="abs" style="left:575px;top:146px;font-size:12px;line-height:22px">
    <div>☎&nbsp;&nbsp; +61 2 5550 1842</div>
    <div>✉&nbsp;&nbsp; info@bellcroftbuild.com</div>
    <div style="margin-top:20px;display:flex;gap:10px"><svg width="10" height="14" viewBox="0 0 10 14"><path d="M5 0a5 5 0 0 0-5 5c0 4 5 9 5 9s5-5 5-9a5 5 0 0 0-5-5z" fill="#fff"/><circle cx="5" cy="5" r="2" fill="#58595b"/></svg><span>48 Ridgeway Ave.<br>Elmvale, NSW 2795</span></div>
  </div>
  <h5 style="left:811px">Contact us</h5>
  <div class="field" style="left:811px;top:142px;width:102px;height:30px">Name</div>
  <div class="field" style="left:917px;top:142px;width:102px;height:30px">Phone</div>
  <div class="field" style="left:1023px;top:142px;width:102px;height:30px">Email</div>
  <div class="field" style="left:811px;top:178px;width:314px;height:56px">Message</div>
  <div class="btn" style="left:811px;top:240px;width:133px;height:27px">Send</div>
  <p class="abs" style="left:74px;top:390px;font-size:11px">Copyright © 2020 BELLCROFT CONSTRUCTION . All Rights Reserved</p>
</footer>
<div class="social" style="left:864px" aria-label="Social link"></div>
<div class="social" style="left:919px" aria-label="Social link"></div>
<div class="social" style="left:974px" aria-label="Social link"></div>
<div class="social" style="left:1030px" aria-label="Social link"></div>
<div class="social" style="left:1082px" aria-label="Social link"></div>

</body>
</html>
```